Fold and Fly travel bag design

I want a design-proposal for a fold and fly travel bag. There is an example attached of the product but I want something much more classy. Maybe with prints on like the bra and panties but more simplistic. In one compartment you will have clean underwear when you travel and in the other one you put the ones for laundry. I will attach our logo as well and I would like to place it somewhere in the design but not sure where, maybe just as a tag/flap on the side. Please use your imagination and creativity. The fold and fly will come in black and beige so rather no other colors than these.

Target Market(s)

Women 18-35

Requirements
Should not have
• Too young design, not to messy! I want it simplistic!

```html
<!DOCTYPE html>
<html lang="en">
<head>
<meta charset="utf-8">
<title>Lumen Carry – Travel Bag Proposal</title>
<link href="https://fonts.googleapis.com/css2?family=Montserrat:wght@400&display=swap" rel="stylesheet">
<style>
  :root {
    --bg: #000000;
    --fabric-dark: #040506;
    --fabric-mid: #0b0c0d;
    --fabric-light: #121314;
    --line: #d6d2c8;
    --text: #f2f0ea;
  }
  html, body {
    margin: 0;
    padding: 0;
    width: 1200px;
    height: 1200px;
    overflow: hidden;
    background: var(--bg);
  }
  .canvas {
    position: relative;
    width: 1200px;
    height: 1200px;
    background: var(--bg);
    font-family: "Montserrat", "Helvetica Neue", Arial, sans-serif;
  }
  .compartment {
    position: absolute;
    top: 398px;
    width: 468px;
    height: 468px;
    border: 1px solid var(--line);
    border-radius: 8px;
    box-sizing: border-box;
    overflow: hidden;
  }
  .compartment--wear { left: 122px; }
  .compartment--wash { left: 591px; }
  .fabric {
    position: absolute;
    inset: 0;
  }
  .compartment--wear .fabric {
    background:
      radial-gradient(ellipse 40% 30% at 22% 20%, var(--fabric-light) 0%, transparent 70%),
      radial-gradient(ellipse 35% 45% at 80% 35%, var(--fabric-light) 0%, transparent 70%),
      radial-gradient(ellipse 45% 25% at 35% 80%, var(--fabric-light) 0%, transparent 70%),
      var(--fabric-dark);
  }
  .compartment--wash .fabric {
    background:
      radial-gradient(ellipse 60% 50% at 40% 30%, var(--fabric-mid) 0%, transparent 75%),
      radial-gradient(ellipse 50% 40% at 70% 80%, var(--fabric-mid) 0%, transparent 75%),
      var(--fabric-dark);
  }
  .compartment__label {
    position: absolute;
    margin: 0;
    font-size: 17px;
    font-weight: 400;
    letter-spacing: 0.28em;
    line-height: 1;
    color: var(--text);
  }
  .compartment--wear .compartment__label { left: 99px; top: 101px; }
  .compartment--wash .compartment__label { left: 99px; top: 96px; }
  .print {
    position: absolute;
    inset: 0;
  }
  .tag {
    position: absolute;
    top: 403px;
    display: flex;
    align-items: center;
    gap: 10px;
    font-size: 10px;
    letter-spacing: 0.16em;
    text-transform: uppercase;
    color: var(--text);
    white-space: nowrap;
  }
  .tag__mark {
    width: 38px;
    height: 38px;
    border: 2px solid var(--line);
    border-radius: 50%;
    box-sizing: border-box;
    flex: none;
  }
  .compartment--wear .tag { left: 30px; }
  .compartment--wash .tag { right: 30px; flex-direction: row-reverse; }
</style>
</head>
<body>
<main class="canvas">
  <section class="compartment compartment--wear">
    <div class="fabric" role="img" aria-label="Black linen fabric with soft folds"></div>
    <h2 class="compartment__label">WEAR</h2>
    <svg class="print" width="468" height="468" viewBox="0 0 468 468" aria-hidden="true">
      <circle cx="164" cy="263" r="67" fill="none" stroke="var(--line)" stroke-width="2.5"/>
      <circle cx="301" cy="263" r="67" fill="none" stroke="var(--line)" stroke-width="2.5"/>
    </svg>
    <div class="tag"><span class="tag__mark"></span><span class="tag__name">Lumen Carry</span></div>
  </section>

  <section class="compartment compartment--wash">
    <div class="fabric" role="img" aria-label="Black linen fabric texture"></div>
    <h2 class="compartment__label">WASH</h2>
    <svg class="print" width="468" height="468" viewBox="0 0 468 468" aria-hidden="true">
      <rect x="98" y="192" width="271" height="136" fill="none" stroke="var(--line)" stroke-width="2.5"/>
      <line x1="233" y1="192" x2="233" y2="328" stroke="var(--line)" stroke-width="2.5"/>
    </svg>
    <div class="tag"><span class="tag__mark"></span><span class="tag__name">Lumen Carry</span></div>
  </section>
</main>
</body>
</html>
```